Redesign Employer Form

We need to consolidate the form located at: BrambleQuarry.com to be one form instead of the multiple screens that currently exist. The new form must be user friendly with a layout that supports the collection of the various pieces of information currently displayed on the site.

```html
<!DOCTYPE html>
<html lang="en">
<head>
<meta charset="utf-8">
<title>BrambleQuarry.com – Salaried Employee</title>
<link href="https://fonts.googleapis.com/css2?family=Raleway:wght@400;500;600;700&family=Open+Sans:wght@600;700&display=swap" rel="stylesheet">
<style>
:root{
  --page:#f6f6f6;
  --header:#1a4aa8;
  --header-dark:#123a8c;
  --navy:#1c3d8e;
  --ink:#4a4a4a;
  --muted:#8a8a8a;
  --border:#cfd7ee;
  --field-border:#d4d4d4;
  --optional:#4c9a2b;
  --btn-blue:#1a4aa0;
  --btn-grey:#555555;
  --footer:#1a4aa8;
  --white:#ffffff;
  --burst:#4fae2a;
  --burst-dark:#2f8a1c;
}
*{box-sizing:border-box;margin:0;padding:0}
html,body{width:1200px;height:2341px;overflow:hidden}
body{background:var(--page);font-family:'Raleway',sans-serif;color:var(--ink);position:relative;font-variant-numeric:lining-nums}
.abs{position:absolute}

/* header */
.site-header{position:absolute;left:0;top:0;width:1200px;height:100px;background:linear-gradient(180deg,var(--header) 0%,var(--header-dark) 100%);overflow:hidden}
.brand-mark{left:100px;top:13px;width:74px;height:74px;border-radius:50%;background:var(--white)}
.brand-name{left:190px;top:33px;font-size:28px;font-weight:700;color:var(--white)}
.region-map{left:940px;top:0;width:260px;height:100px;background:linear-gradient(120deg,rgba(255,255,255,0) 0%,rgba(120,160,220,.45) 60%,rgba(90,130,200,.5) 100%)}

/* promo badge */
.promo-badge{position:absolute;left:790px;top:-20px;width:128px;height:128px;border-radius:50%;background:radial-gradient(circle at 45% 40%,#7cd14a 0%,var(--burst) 55%,var(--burst-dark) 100%);border:3px solid var(--white);text-align:center;font-weight:700;line-height:1}
.promo-badge .line1{position:absolute;left:0;right:0;top:28px;font-size:18px;color:var(--white)}
.promo-badge .line2{position:absolute;left:0;right:0;top:48px;font-size:18px;color:#14240c}
.promo-badge .price{position:absolute;left:0;right:0;top:72px;font-size:23px;color:var(--white)}

/* title */
.form-title{left:97px;top:142px;font-size:26px;font-weight:600;color:var(--navy)}
.title-rule{left:97px;top:183px;width:1005px;height:2px;background:var(--navy)}
.collapse-icon{left:1088px;top:156px;width:14px;height:14px}

/* cards */
.card{position:absolute;left:98px;width:1002px;background:var(--white);border:2px solid var(--border)}
.card-title{position:absolute;left:20px;font-size:21px;font-weight:500;color:var(--navy)}
.card-rule{position:absolute;left:20px;width:961px;height:1px;background:#e6e6e6}
.label{position:absolute;font-size:14px;color:var(--ink);line-height:1.5}
.field{position:absolute;height:36px;border:1px solid var(--field-border);background:var(--white);font-size:12px}
.field .hint{position:absolute;right:8px;top:11px;font-size:10px;color:var(--optional)}
.field .value{position:absolute;left:12px;top:9px;font-size:14px;color:var(--navy)}
.field .placeholder{position:absolute;left:10px;top:9px;font-size:14px;color:var(--ink)}
.select .chev{position:absolute;right:12px;top:12px;width:10px;height:10px}
.radio{position:absolute;font-size:14px;color:var(--ink);display:flex;align-items:center;gap:14px}
.radio .dot{width:13px;height:13px;border-radius:50%;border:1px solid #aaa;background:#e8e8e8}
.radio.checked{color:var(--navy)}
.radio.checked .dot{background:var(--white);border:1px solid #2a6ac8;box-shadow:inset 0 0 0 3px var(--white),inset 0 0 0 7px #2a6ac8}
.toggle{position:absolute;height:42px;border:1px solid var(--field-border);display:flex;align-items:center;justify-content:center;gap:12px;font-size:12.5px;color:var(--muted)}
.toggle .dot{width:12px;height:12px;border-radius:50%;border:1px solid #aaa;background:#e8e8e8}
.para{position:absolute;left:22px;width:880px;font-size:13px;line-height:30px;color:var(--ink)}
.list-link{position:absolute;left:28px;font-size:15px;color:var(--navy);display:flex;gap:14px}
.list-link .action{color:var(--ink);font-size:14px;margin-left:6px}
.sub-title{position:absolute;left:24px;font-size:21px;font-weight:500;color:var(--navy)}

/* buttons */
.btn{position:absolute;top:1985px;height:45px;width:236px;border-radius:2px;font-family:'Open Sans',sans-serif;font-weight:600;font-size:17px;color:var(--white);display:flex;align-items:center;justify-content:center}
.btn-primary{background:var(--btn-blue)}
.btn-secondary{background:var(--btn-grey)}

/* footer */
.site-footer{position:absolute;left:0;top:2097px;width:1200px;height:244px;background:var(--footer)}
.trust-badge{position:absolute;top:44px;width:182px;height:75px;border:2px solid rgba(255,255,255,.25);background:rgba(0,0,0,.08)}
.trust-badge span{position:absolute;left:22px;top:14px;width:136px;height:45px;background:var(--white);border-radius:4px}
.footer-links{position:absolute;left:0;width:1200px;top:155px;text-align:center;font-size:14px;color:var(--white)}
.copyright{position:absolute;left:0;width:1200px;top:192px;text-align:center;font-size:14px;color:var(--white)}
.build-code{position:absolute;left:1130px;top:206px;font-size:12px;font-weight:700;color:var(--white)}
</style>
</head>
<body>

<header class="site-header">
  <div class="abs brand-mark"></div>
  <div class="abs brand-name">BrambleQuarry.com</div>
  <div class="abs region-map" role="img" aria-label="Faint state map decoration"></div>
  <div class="promo-badge">
    <span class="line1">Instant</span>
    <span class="line2">Delivery</span>
    <span class="price">$7.95</span>
  </div>
</header>

<h1 class="abs form-title">Salaried Employee</h1>
<svg class="abs collapse-icon" viewBox="0 0 14 14"><path d="M3 2l4 4 4-4M3 7l4 4 4-4" fill="none" stroke="var(--navy)" stroke-width="1.6"/></svg>
<div class="abs title-rule"></div>

<!-- Company -->
<section class="card" style="top:231px;height:276px">
  <h2 class="card-title" style="top:26px">Company Information:</h2>
  <div class="card-rule" style="top:64px"></div>
  <div class="label" style="left:20px;top:108px">Company Name*</div>
  <div class="field" style="left:162px;top:101px;width:820px"></div>
  <div class="label" style="left:20px;top:162px">Company Address</div>
  <div class="field" style="left:162px;top:153px;width:321px"><span class="hint">Optional*</span></div>
  <div class="label" style="left:521px;top:162px">Company Zip Code</div>
  <div class="field" style="left:669px;top:153px;width:312px"><span class="hint">Optional*</span></div>
  <div class="label" style="left:20px;top:213px">Phone Number</div>
  <div class="field" style="left:162px;top:205px;width:321px"><span class="hint">Optional*</span></div>
  <div class="label" style="left:521px;top:213px">Company EIN / SSN</div>
  <div class="field" style="left:669px;top:205px;width:312px"><span class="hint">Optional*</span></div>
</section>

<!-- Employee -->
<section class="card" style="top:546px;height:411px">
  <h2 class="card-title" style="top:32px">Employee Information:</h2>
  <div class="card-rule" style="top:70px"></div>
  <div class="label" style="left:20px;top:122px">Employee Name*</div>
  <div class="field" style="left:162px;top:115px;width:820px"></div>
  <div class="label" style="left:20px;top:176px">Employee Address</div>
  <div class="field" style="left:162px;top:169px;width:820px"><span class="hint">Optional*</span></div>
  <div class="label" style="left:20px;top:230px">Employee SSN</div>
  <div class="field" style="left:162px;top:222px;width:321px"><span class="hint">(Last 4 digits)*</span></div>
  <div class="label" style="left:521px;top:230px">Employee ID</div>
  <div class="field" style="left:669px;top:222px;width:312px"><span class="hint">Optional*</span></div>
  <div class="label" style="left:20px;top:282px">Employee Zip Code</div>
  <div class="field" style="left:162px;top:274px;width:321px"><span class="hint">Optional*</span></div>
  <div class="label" style="left:521px;top:282px">Dependants</div>
  <div class="field select" style="left:669px;top:274px;width:312px"><span class="placeholder" style="font-size:12px">0</span><svg class="chev" viewBox="0 0 10 10"><path d="M2 3l3 3 3-3" fill="none" stroke="#666"/></svg></div>
  <div class="label" style="left:20px;top:334px">Marital Status</div>
  <div class="field" style="left:162px;top:327px;width:321px"><span class="hint">Optional*</span></div>
  <div class="label" style="left:521px;top:334px">Age 65 And &gt;&gt;<br>Blind Exemptions</div>
  <div class="field select" style="left:669px;top:327px;width:312px"><span class="placeholder" style="font-size:12px">0</span><svg class="chev" viewBox="0 0 10 10"><path d="M2 3l3 3 3-3" fill="none" stroke="#666"/></svg></div>
</section>

<!-- Salary -->
<section class="card" style="top:999px;height:410px">
  <h2 class="card-title" style="top:28px">Salary Information:</h2>
  <div class="card-rule" style="top:67px"></div>
  <div class="label" style="left:24px;top:114px">Annual Salary*</div>
  <div class="field" style="left:162px;top:108px;width:320px"><span class="value" style="font-size:13px">$ 234561.00</span></div>
  <div class="label" style="left:508px;top:114px">Choose First Pay Date(s)<br>&nbsp;Needed*</div>
  <div class="field" style="left:679px;top:108px;width:303px"><span class="hint">Optional*</span></div>

  <div class="radio" style="left:69px;top:202px"><span class="dot"></span>Weekly (Ex: Every Friday)</div>
  <div class="radio checked" style="left:345px;top:202px"><span class="dot"></span>Daily</div>
  <div class="radio" style="left:484px;top:202px"><span class="dot"></span>Semi-Monthly (Ex: 1st and 16th)</div>
  <div class="radio" style="left:788px;top:202px"><span class="dot"></span>Semi-Annually</div>
  <div class="radio" style="left:69px;top:246px"><span class="dot"></span>Monthly (Ex: 1st of month only)</div>
  <div class="radio" style="left:345px;top:246px"><span class="dot"></span>Quarterly</div>
  <div class="radio" style="left:484px;top:246px"><span class="dot"></span>Bi-Weekly (Ex: Every other Wed.)</div>
  <div class="radio" style="left:788px;top:246px"><span class="dot"></span>Quarterly</div>

  <div class="toggle" style="left:151px;top:320px;width:307px"><span class="dot"></span>This employee was hired in 2016</div>
  <div class="toggle" style="left:507px;top:320px;width:284px"><span class="dot"></span>Show hourly rate on the stub</div>
</section>

<!-- Additional -->
<section class="card" style="top:1453px;height:467px">
  <h2 class="card-title" style="top:30px;left:22px">Additional Income and Deductions:</h2>
  <div class="card-rule" style="top:70px;left:22px"></div>
  <p class="para" style="top:92px">In addition to your pay and standard withholdings, add additional income and / or deductions. Additions and Deductions will be applied to each pay date requested below.</p>
  <div class="list-link" style="top:176px"><span>»</span>Additions (Description / Current Amount / YTD Amount)<span class="action">Add Income</span></div>
  <div class="list-link" style="top:212px"><span>»</span>Deductions (Description / Current Amount / YTD Amount)<span class="action">Add Deduction</span></div>
  <h2 class="sub-title" style="top:268px">Check Numbers:</h2>
  <p class="para" style="top:306px">For your convenience, we have auto generated check numbers for each pay date you selected. Keep, modify, or delete the check numb ers from your stubs.</p>
  <div class="field" style="left:28px;top:392px;width:454px"><span class="placeholder">Date</span>
    <svg style="position:absolute;right:10px;top:11px" width="14" height="13" viewBox="0 0 14 13"><rect x="1" y="2" width="12" height="10" fill="none" stroke="#777"/><path d="M1 5h12M4 0v3M10 0v3M4 8h2M8 8h2" stroke="#777"/></svg>
  </div>
  <div class="field" style="left:501px;top:392px;width:382px"><span class="placeholder">Check #</span></div>
</section>

<div class="btn btn-primary" style="left:223px">Submit and Preview</div>
<div class="btn btn-secondary" style="left:473px">Make Changes</div>
<div class="btn btn-primary" style="left:724px">Download Your Stub</div>

<footer class="site-footer">
  <div class="trust-badge" style="left:401px"><span></span></div>
  <div class="trust-badge" style="left:615px"><span></span></div>
  <div class="footer-links">Looking for another state &nbsp;/&nbsp; Problem with your stub delivery? &nbsp;/&nbsp; finished paystub sample &nbsp;/&nbsp; About Us &nbsp;/&nbsp; Features &nbsp;/&nbsp; FAQ</div>
  <div class="copyright">All Rights Reserved . Copyrights2016@companyname.com</div>
  <div class="build-code">C18</div>
</footer>

</body>
</html>
```